M&A Advisory firm needs elegant and powerful letterhead

We need a powerful but elegant letterhead to engage with the international financial industry.

Target Market(s)

New York and International Financial Industry

Industry/Entity Type

Finance

Font styles to use
Other font styles liked:
• Poppins

Requirements
Must have
• 482 W 71st Street 14th Floor New York, NY 10157 O: +1 (212) 555 0147 F: +1 (212) 555 0182

```html
<!DOCTYPE html>
<html lang="en">
<head>
<meta charset="utf-8">
<title>Meridant Letterhead</title>
<link rel="stylesheet" href="https://fonts.googleapis.com/css2?family=Arimo:wght@400&family=Poppins:wght@400;600&display=swap">
<style>
  :root {
    --bg: #d9d9d9;
    --paper: #e7e7e7;
    --brand-blue: #0b4884;
    --brand-gray: #77787b;
    --ink: #4a4a4a;
    --ink-soft: #6b6b6b;
    --rule: #9a9a9a;
  }
  * { margin: 0; padding: 0; box-sizing: border-box; }
  html, body { width: 1200px; height: 1024px; overflow: hidden; background: var(--bg); }
  .letterhead {
    position: absolute; left: 260px; top: 32px;
    width: 679px; height: 960px;
    background: var(--paper);
    box-shadow: 0 6px 24px rgba(0,0,0,0.18);
    overflow: hidden;
  }
  .brand-name {
    position: absolute; left: 47px; top: 78px;
    font-family: "Poppins", sans-serif; font-weight: 600;
    font-size: 26px; line-height: 1; color: var(--ink); letter-spacing: 2px;
  }
  .contact {
    position: absolute; left: 476px; top: 61px;
    font-style: normal;
    font-family: "Arimo", sans-serif; font-size: 11px; line-height: 13px; color: var(--ink-soft);
  }
  .contact-row { display: flex; align-items: center; gap: 3px; }
  .contact-icon { width: 9px; height: 9px; }
  .contact-address { margin-top: 5px; }
  .header-rule {
    position: absolute; left: 47px; top: 123px; width: 584px; height: 1px; background: var(--rule);
  }
  .letter { position: absolute; left: 61px; top: 292px; width: 556px; color: var(--ink); }
  .salutation { font-family: "Poppins", sans-serif; font-weight: 600; font-size: 15px; line-height: 22px; margin-bottom: 24px; }
  .letter p.body {
    font-family: "Arimo", sans-serif; font-size: 11.8px; line-height: 14px; margin-bottom: 12px;
  }
  .closing { font-family: "Poppins", sans-serif; font-weight: 600; font-size: 9px; margin-top: 20px; }
  .signature {
    width: 112px; height: 30px; margin-top: 26px;
    background: linear-gradient(90deg, rgba(74,74,74,0.25), rgba(74,74,74,0.12));
    border-radius: 3px;
  }
  .footer-band { position: absolute; left: 0; bottom: 0; width: 679px; height: 46px; background: var(--brand-blue); }
  .footer-line { position: absolute; left: 0; bottom: 52px; width: 679px; height: 4px; background: var(--brand-gray); }
</style>
</head>
<body>
  <main class="letterhead">
    <header>
      <div class="brand-name">MERIDANT</div>
      <address class="contact">
        <div class="contact-row">
          <svg class="contact-icon" viewBox="0 0 10 10"><path d="M2 1 L3.6 1 L4.2 3 L3.2 3.8 C3.8 5 4.9 6.1 6.2 6.8 L7 5.8 L9 6.4 L9 8 C9 8.6 8.5 9 8 9 C4.2 8.8 1.2 5.8 1 2 C1 1.5 1.4 1 2 1 Z" fill="var(--brand-blue)"/></svg>
          <span>+1 (212) 555 0147</span>
        </div>
        <div class="contact-row">
          <svg class="contact-icon" viewBox="0 0 10 10"><rect x="2.5" y="1" width="5" height="3" fill="none" stroke="var(--brand-blue)" stroke-width="1"/><rect x="1" y="4" width="8" height="5" rx="1" fill="none" stroke="var(--brand-blue)" stroke-width="1"/><line x1="3" y1="6.5" x2="7" y2="6.5" stroke="var(--brand-blue)" stroke-width="1"/></svg>
          <span>+1 (212) 555 0182</span>
        </div>
        <div class="contact-address">482 W 71st Street<br>14th Floor New York, NY 10157</div>
      </address>
      <div class="header-rule"></div>
    </header>

    <section class="letter">
      <h1 class="salutation">Dear Mr. Carter,</h1>
      <p class="body">Lorem ipsum dolor sit amet, consectetuer adipiscing elit, sed diam nonmmy nibh euismod tincidunt ut laor eet dolore magna aliquam erat volutpat. Ut wisi enim ad minim veniam, quis nostrud exerci tationmcorper suscipit lobortis nisl ut aliquip ex ea commodo consequat. Duis autem vel eum iriure dolor in hendrerit in vulputate velit esse molestie consequat, vel illum dolore eu feugiat</p>
      <p class="body">Rorem ipsum dolor sit amet, consectetuer adipiscing elit, sed diam nonmmy nibh euismod tincidunt ut laor eet dolore magna aliquam erat volutpat. Ut wisi enim ad minim veniam, quis nostrud exerci tationmcorper suscipit lobortis nisl ut aliquip ex ea commodo consequat. Duis autem vel eum iriure dolor in hendrerit in vulputate velit esse molest</p>
      <p class="body">Dorem ipsum dolor sit amet, consectetuer adipiscing elit, sed diam nonmmy nibh euismod tincidunt ut laor eet dolore magna aliquam erat volutpat. Ut wisi enim ad minim veniam, quis nostrud exerci tationmcorper suscipit lobortis nisl ut aliquip ex ea commodo consequat. Duis autem vel eum iriure dolor in hendrerit in suscipit lobortis nisl ut aliquip ex ea commodo consequat. Duis autem vel eum iriure dolor in hendrerit in vulputate velit esse molestie consequat, vel illum</p>
      <p class="body">Sorem ipsum dolor sit amet, consectetuer adipiscing elit, sed diam nonmmy nibh euismod tincidunt ut laor eet dolore magna aliquam erat volutpat. Ut wisi enim ad minim veniam, quis nostrud exerci tationmcorper suscipit lobortis nisl ut aliquip ex ea commodo consequat. Duis autem vel eum iriure dolor in</p>
      <p class="closing">Sincerely,</p>
      <div class="signature" role="img" aria-label="Handwritten signature of the sender"></div>
    </section>

    <footer>
      <div class="footer-line"></div>
      <div class="footer-band"></div>
    </footer>
  </main>
</body>
</html>
```